Spray Foam Company Business Card

We need a business card designed for our spray foam insulation and roof coatings business. We handle residential and commercial projects.
Construction
We would like it to say:
R & K Spray
with these bullet points
-foam insulation
-waterproofing roof system
-water proofing foundation systems
website is rksprayfoaminsulation.example (this was just purchased)
office phone : 630-482-9164
And 3 cards with names on them the names are :
Derek Halvorsen
Curtis Pennington
Rob Stallworth
maybe the bullet points can go on the back?
if you go this website it is another division of our company and you can see the font we use in the R & K. We do not want to use the same half circles that it has just the lettering
www.coatedrightforyears.example

```html
<!DOCTYPE html>
<html lang="en">
<head>
<meta charset="utf-8">
<title>R &amp; K Spray — Business Card</title>
<link rel="stylesheet" href="https://fonts.googleapis.com/css2?family=Open+Sans:wght@400;700&display=swap">
<style>
  :root {
    --stage: #2b2b2b;
    --ink: #0b0b0b;
    --paper: #ffffff;
    --rule: #9a9a9a;
    --faint: #dcdcdc;
  }
  * { box-sizing: border-box; margin: 0; padding: 0; }
  html, body { width: 1200px; height: 900px; overflow: hidden; }
  body {
    background: var(--stage);
    font-family: "Open Sans", Arial, sans-serif;
    position: relative;
  }
  .card {
    position: absolute;
    left: 300px;
    width: 600px;
    height: 343px;
    overflow: hidden;
    box-shadow: 0 10px 24px rgba(0,0,0,.45);
  }
  /* Back side */
  .card-back { top: 62px; background: var(--ink); color: var(--paper); }
  .card-back .brand-mark {
    position: absolute; right: 40px; top: 34px;
    display: flex; align-items: center; gap: 12px;
    font-size: 46px; font-weight: 400; letter-spacing: 1px; color: var(--paper);
  }
  .brand-dot { width: 14px; height: 14px; border-radius: 50%; background: currentColor; }
  .card-back .top-rule {
    position: absolute; left: 250px; right: 18px; top: 124px;
    border-top: 1px solid var(--rule);
  }
  .card-back .site {
    position: absolute; right: 32px; top: 136px;
    font-size: 14px; letter-spacing: .3px;
  }
  .card-back .bottom-rule {
    position: absolute; left: 132px; right: 0; top: 188px;
    border-top: 1px solid var(--rule);
  }
  .card-back .services {
    position: absolute; left: 26px; top: 222px;
  }
  .services h2 { font-size: 15px; font-weight: 700; margin-bottom: 2px; }
  .services ul { list-style: none; }
  .services li {
    font-size: 14px; line-height: 19px;
    display: flex; align-items: center; gap: 9px;
  }
  .services li::before {
    content: ""; width: 9px; height: 9px; border-radius: 50%; background: var(--paper);
  }
  /* Front side */
  .card-front { top: 475px; background: var(--paper); }
  .card-front .band { position: absolute; inset: 0; }
  .card-front .brand-mark {
    position: absolute; left: 34px; top: 48px;
    display: flex; align-items: center; gap: 10px;
    font-size: 42px; font-weight: 400; color: var(--ink);
  }
  .card-front .brand-ghost {
    position: absolute; right: 34px; top: 118px;
    font-size: 56px; font-weight: 400; color: var(--faint);
  }
  .card-front .contact {
    position: absolute; left: 34px; top: 232px; color: var(--paper);
  }
  .contact .name {
    font-size: 20px; font-weight: 700; letter-spacing: .8px; text-transform: uppercase;
    margin-bottom: 10px;
  }
  .contact p {
    font-size: 14px; line-height: 21px; display: flex; align-items: center; gap: 10px;
  }
  .contact svg { width: 13px; height: 13px; fill: none; stroke: var(--paper); stroke-width: 1.6; }
</style>
</head>
<body>

<section class="card card-back">
  <div class="brand-mark">R &amp; K<span class="brand-dot"></span></div>
  <div class="top-rule"></div>
  <p class="site">www.coatedrightforyears.example</p>
  <div class="bottom-rule"></div>
  <div class="services">
    <h2>R &amp; K Spray</h2>
    <ul>
      <li>Foam insulation</li>
      <li>Waterproofing roof system</li>
      <li>Water proofing foundation systems</li>
    </ul>
  </div>
</section>

<section class="card card-front">
  <svg class="band" viewBox="0 0 600 343" preserveAspectRatio="none" aria-hidden="true">
    <path d="M0 200 H330 C360 200 370 175 400 140 C430 100 470 70 520 66 L600 62 V343 H0 Z" fill="#0b0b0b"/>
    <path d="M372 200 C390 150 440 95 530 88 C575 85 600 100 600 100 V250 C560 262 500 258 450 240 C410 226 380 215 372 200 Z" fill="#ffffff"/>
  </svg>
  <div class="brand-mark">R &amp; K<span class="brand-dot"></span></div>
  <div class="brand-ghost">R &amp; K</div>
  <div class="contact">
    <h1 class="name">Derek Halvorsen</h1>
    <p>
      <svg viewBox="0 0 14 14"><path d="M2 5 C4 2 10 2 12 5 L11 7 L9 6 L9 5 C7.5 4.5 6.5 4.5 5 5 L5 6 L3 7 Z M3 8 H11 V12 H3 Z"/></svg>
      630-482-9164
    </p>
    <p>
      <svg viewBox="0 0 14 14"><circle cx="7" cy="7" r="5.5"/><path d="M1.5 7 H12.5 M7 1.5 C4 4.5 4 9.5 7 12.5 M7 1.5 C10 4.5 10 9.5 7 12.5"/></svg>
      www.rksprayfoaminsulation.example
    </p>
  </div>
</section>

</body>
</html>
```